The name of the company is Torvend Holdings, LLC. I would like a business card with a logo.

On the top left, I would like a logo design of a crown and I would like Torvend over the top of the crown while Holdings on the bottom. Please see attached files as an example of crown and positioning of Torvend Holdings. Then I would like the letters TH in the middle(see picture).

Colors

Designer to choose colors to be used in the design.

```html
<!DOCTYPE html>
<html lang="en">
<head>
<meta charset="utf-8">
<title>Torvend Holdings, LLC — Business Card</title>
<link href="https://fonts.googleapis.com/css2?family=Lato:wght@400;700&display=swap" rel="stylesheet">
<style>
  :root {
    --backdrop: #3a332e;
    --card: #121212;
    --card-edge: #1c1c1c;
    --gold: #f2c21b;
    --silver: #c9c9c9;
    --silver-soft: #9a9a9a;
    --divider: #3a3a3a;
  }
  * { margin: 0; padding: 0; box-sizing: border-box; }
  html, body {
    width: 1200px; height: 844px; overflow: hidden;
    background: var(--backdrop);
    font-family: "Lato", Arial, sans-serif;
  }
  .stage {
    width: 1200px; height: 844px;
    display: flex; align-items: center; justify-content: center; gap: 60px;
  }
  .card {
    width: 525px; height: 300px;
    background: var(--card);
    border: 1px solid var(--card-edge);
    border-radius: 3px;
    box-shadow: 0 14px 30px rgba(0,0,0,.45);
    position: relative;
  }
  .card-front { display: flex; align-items: center; }
  .brand-block {
    width: 220px; height: 100%;
    display: flex; align-items: center; justify-content: center;
  }
  .brand-name {
    color: var(--silver);
    font-weight: 700;
    font-size: 24px;
    line-height: 1.2;
    letter-spacing: 2px;
    text-transform: uppercase;
    text-align: center;
  }
  .divider {
    width: 1px; height: 190px;
    background: linear-gradient(to bottom, transparent, var(--divider), transparent);
  }
  .contact-block { padding-left: 30px; color: var(--silver); }
  .person-name {
    color: var(--gold); font-weight: 700; font-size: 19px;
    letter-spacing: .5px; text-transform: uppercase;
  }
  .person-name .credential { font-size: 13px; font-weight: 400; }
  .person-title { font-size: 13px; margin-bottom: 8px; color: var(--silver); }
  .contact-line { display: flex; align-items: center; gap: 7px; font-size: 13px; line-height: 1.55; }
  .contact-line svg { width: 12px; height: 12px; fill: var(--gold); flex: none; }
  .company-name {
    margin-top: 12px; color: var(--gold); font-size: 14px;
    text-transform: uppercase; letter-spacing: .5px;
  }
  .address { font-size: 14px; line-height: 1.4; }
  .card-back { display: flex; align-items: center; justify-content: center; }
  .back-brand {
    color: var(--silver); font-weight: 700; font-size: 30px;
    letter-spacing: 3px; text-transform: uppercase; text-align: center; line-height: 1.25;
  }
</style>
</head>
<body>
<main class="stage">
  <section class="card card-front" aria-label="Business card front">
    <div class="brand-block">
      <p class="brand-name">Torvend<br>Holdings, LLC</p>
    </div>
    <div class="divider"></div>
    <div class="contact-block">
      <h1 class="person-name">Daren Kolvesti, <span class="credential">MBA</span></h1>
      <p class="person-title">Founder / CEO</p>
      <p class="contact-line">
        <svg viewBox="0 0 24 24" aria-hidden="true"><path d="M6.6 10.8a15.1 15.1 0 0 0 6.6 6.6l2.2-2.2a1 1 0 0 1 1-.25 11.4 11.4 0 0 0 3.6.57 1 1 0 0 1 1 1V20a1 1 0 0 1-1 1A17 17 0 0 1 3 4a1 1 0 0 1 1-1h3.5a1 1 0 0 1 1 1c0 1.25.2 2.45.57 3.57a1 1 0 0 1-.25 1z"/></svg>
        (310) 555-0147
      </p>
      <p class="contact-line">
        <svg viewBox="0 0 24 24" aria-hidden="true"><path d="M2 5h20v14H2z M2 5l10 8 10-8" stroke="#121212" stroke-width="1.6"/></svg>
        torvendholdings@mailbox.com
      </p>
      <p class="company-name">Torvend Holdings, LLC</p>
      <p class="address">418 Alder Crest Drive Suite 200<br>Lindale Heights, CA 90388</p>
    </div>
  </section>

  <section class="card card-back" aria-label="Business card back">
    <p class="back-brand">Torvend<br>Holdings</p>
  </section>
</main>
</body>
</html>
```